Banner for fencing on construction sites

Banner to market our company on construction job sites Included on banner we would need something along the lines "Temp Labor" and our website "WWW.KTRVB.COM" all Visible enough to see as people are driving by.
The attached .ai file we provided has two images, we prefer the 2nd one with just RVB.
The Banner will be 7ft wide x 4ft height.

Target Market(s)

Construction Companies

Requirements
Must have
• Visible Website to drivers passing by
• RVB Logo has to be BIGGER than anything

```html
<!DOCTYPE html>
<html lang="en">
<head>
<meta charset="utf-8">
<title>RVB Temp Labor – Site Fence Banner</title>
<link rel="stylesheet" href="https://fonts.googleapis.com/css2?family=Open+Sans:wght@700;800&display=swap">
<style>
  :root {
    --page-bg: #e9eaec;
    --banner-black: #0a0505;
    --frame-white: #ffffff;
    --brand-orange: #f27a12;
    --ink-black: #111111;
  }
  * { margin: 0; padding: 0; box-sizing: border-box; }
  html, body {
    width: 1200px;
    height: 900px;
    overflow: hidden;
    background: var(--page-bg);
    font-family: "Open Sans", Arial, sans-serif;
  }
  .banner {
    position: absolute;
    left: 40px;
    top: 130px;
    width: 1120px;
    height: 640px;
    background: var(--banner-black);
    box-shadow: 0 10px 30px rgba(0,0,0,0.25);
  }
  .banner-art {
    position: absolute;
    inset: 0;
    width: 1120px;
    height: 640px;
  }
  .brand-name {
    position: absolute;
    left: 0;
    right: 0;
    top: 118px;
    text-align: center;
    font-weight: 800;
    font-size: 210px;
    line-height: 1;
    letter-spacing: -4px;
    color: var(--brand-orange);
  }
  .service-line {
    position: absolute;
    left: 300px;
    top: 410px;
    font-weight: 800;
    font-size: 80px;
    line-height: 1;
    color: var(--brand-orange);
    letter-spacing: 1px;
  }
  .web-address {
    position: absolute;
    left: 200px;
    width: 720px;
    top: 527px;
    text-align: center;
    font-weight: 800;
    font-size: 64px;
    line-height: 1;
    color: var(--ink-black);
    letter-spacing: -1px;
  }
  .web-address .domain { color: var(--brand-orange); }
</style>
</head>
<body>
  <main class="banner">
    <svg class="banner-art" viewBox="0 0 1120 640" xmlns="http://www.w3.org/2000/svg">
      <defs>
        <radialGradient id="flame-tone" cx="50%" cy="50%" r="50%">
          <stop offset="0%" stop-color="#d9d9d9" stop-opacity="0.55"/>
          <stop offset="60%" stop-color="#8a8a8a" stop-opacity="0.25"/>
          <stop offset="100%" stop-color="#0a0505" stop-opacity="0"/>
        </radialGradient>
      </defs>

      <path class="frame" fill="none" stroke="var(--frame-white)" stroke-width="7"
            d="M70,40 H1050 A40,40 0 0 0 1090,80 V520 A40,40 0 0 0 1050,560 H70 A40,40 0 0 0 30,520 V80 A40,40 0 0 0 70,40 Z"/>

      <g role="img" aria-label="White tribal flame ornament flaring out from both sides of the brand name">
        <ellipse cx="560" cy="230" rx="440" ry="150" fill="url(#flame-tone)"/>
      </g>

      <path class="ribbon" fill="var(--frame-white)"
            d="M160,510 H960 L925,555 L960,600 H160 L195,555 Z"/>
    </svg>

    <h1 class="brand-name">RVB</h1>
    <p class="service-line">TEMP LABOR</p>
    <p class="web-address">WWW.<span class="domain">KTRVB</span>.COM</p>
  </main>
</body>
</html>
```